Bright Harbor Family Club Business Card Project

We are a Minneapolis based discount club that caters to families with children. We need a business card that can be used to communicate our contact information to other businesses that may wish to offer discounts on our website.

Please use placeholders for contact information (i.e. John Doe, 123 Any Street, Any Town, etc.) and include spaces for the following: Full name, title, email, phone number, website, one line street address, city, state, and zip code.

Reason: I have extended the deadline because I had not intended the project to close so quickly.

Target Market(s)

Most of the time the business cards will be used in business to business situations. However, from time to time they may be distributed to our end customer, families with children.

Industry/Entity Type

Club

Font styles to use
Serif
Sans Serif
Other font styles liked:
• Open to suggestions

Requirements
Nice to have
• We might use the reverse side of the card as the design for our membership card.

```html
<!DOCTYPE html>
<html lang="en">
<head>
<meta charset="utf-8">
<title>Bright Harbor Family Club – Business Card</title>
<link href="https://fonts.googleapis.com/css2?family=Arimo:wght@400;700&display=swap" rel="stylesheet">
<style>
  :root {
    --stage: #0e0e0e;
    --card-brown: #3a2314;
    --border-brown: #4c2d18;
    --frame-orange: #f08a1e;
    --name-red: #c9291f;
    --title-gold: #e3a51c;
    --text-light: #f3ece4;
    --logo-orange: #f5a313;
  }
  * { margin: 0; padding: 0; box-sizing: border-box; }
  html, body {
    width: 1200px; height: 873px; overflow: hidden;
    background: var(--stage);
    font-family: "Arimo", Arial, sans-serif;
  }
  .sheet {
    position: relative; width: 1200px; height: 873px;
    display: flex; align-items: center; justify-content: center; gap: 60px;
  }
  .card {
    position: relative; width: 500px; height: 300px;
    border-radius: 6px; overflow: hidden;
    background: var(--card-brown);
  }
  .card-border {
    position: absolute; inset: 0;
    background: radial-gradient(ellipse at center, var(--card-brown) 55%, var(--border-brown) 100%);
  }
  .card-frame { position: absolute; inset: 0; }
  .card-content { position: absolute; inset: 0; }

  /* front */
  .brand {
    position: absolute; left: 0; right: 0; top: 50%;
    transform: translateY(-50%);
    display: flex; align-items: center; justify-content: center; gap: 10px;
  }
  .brand-dot {
    width: 18px; height: 18px; border-radius: 50%;
    background: var(--logo-orange); flex: none;
  }
  .brand-name {
    font-weight: 700; font-size: 24px; line-height: 1;
    color: var(--logo-orange); white-space: nowrap;
  }

  /* back */
  .contact { position: absolute; left: 66px; top: 40px; }
  .contact-name {
    color: var(--name-red); font-size: 24px; font-weight: 400; line-height: 28px;
  }
  .contact-title {
    color: var(--title-gold); font-size: 13px; line-height: 16px; margin: 4px 0 10px;
  }
  .contact-list { list-style: none; }
  .contact-list li {
    display: flex; align-items: center; gap: 8px;
    color: var(--text-light); font-size: 12px; line-height: 17px;
  }
  .contact-icon {
    width: 11px; height: 11px; border-radius: 50%;
    border: 1.5px solid var(--frame-orange); flex: none;
  }
  .contact-web {
    color: var(--text-light); font-size: 12px; line-height: 16px; margin-top: 4px;
  }
  .brand-small {
    position: absolute; right: 72px; bottom: 56px;
    display: flex; align-items: center; gap: 7px;
  }
  .brand-small .brand-dot { width: 12px; height: 12px; }
  .brand-small .brand-name { font-size: 15px; }
</style>
</head>
<body>
<main class="sheet">

  <section class="card card-front">
    <div class="card-border" role="img" aria-label="Border of fine orange radiating lines"></div>
    <svg class="card-frame" viewBox="0 0 500 300" aria-hidden="true">
      <rect x="34" y="26" width="432" height="248" rx="70" ry="70"
            fill="var(--card-brown)" stroke="var(--frame-orange)" stroke-width="2"/>
    </svg>
    <div class="card-content">
      <div class="brand">
        <span class="brand-dot"></span>
        <span class="brand-name">Bright Harbor Family Club</span>
      </div>
    </div>
  </section>

  <section class="card card-back">
    <div class="card-border" role="img" aria-label="Border of fine orange radiating lines"></div>
    <svg class="card-frame" viewBox="0 0 500 300" aria-hidden="true">
      <rect x="34" y="26" width="432" height="248" rx="70" ry="70"
            fill="var(--card-brown)" stroke="var(--frame-orange)" stroke-width="2"/>
    </svg>
    <div class="card-content">
      <div class="contact">
        <h1 class="contact-name">Mara Ellison</h1>
        <p class="contact-title">Financial Advisor</p>
        <ul class="contact-list">
          <li><span class="contact-icon"></span>48 Lakeview Street</li>
          <li><span class="contact-icon"></span>Minneapolis</li>
          <li><span class="contact-icon"></span>Minnesota</li>
          <li><span class="contact-icon"></span>55401</li>
          <li><span class="contact-icon"></span>mara@brightharbor.com</li>
          <li><span class="contact-icon"></span>01 0123 456 789 0</li>
        </ul>
        <p class="contact-web">www.brightharborclub.com</p>
      </div>
      <div class="brand-small">
        <span class="brand-dot"></span>
        <span class="brand-name">Bright Harbor Family Club</span>
      </div>
    </div>
  </section>

</main>
</body>
</html>
```